2 Business Card Designs

Need two business cards designed:
1) for lumora studio (wedding video) website is lumorastudio.com.au
2) for lumora studio (corporate video) website is lumorastudio.net.au

I am looking for something simple, no fancy shapes etc. Just elegant, simple and classy.

Both companies are video companies, one specialising in weddings the other corporate videos. Neither card needs to have any pics of video or camera related images. Please use same colour schemes as respective websites.

Logo is the same but can change colour.

Industry/Entity Type

Camera

Requirements
Must have
• Logo should be either all white or a colour to match websites
Should not have
• swirls, flowers, shapes, etc.

```html
<!DOCTYPE html>
<html lang="en">
<head>
<meta charset="utf-8">
<title>lumora studio – business card</title>
<link rel="stylesheet" href="https://fonts.googleapis.com/css2?family=Montserrat:wght@300&family=Oswald:wght@300&display=swap">
<style>
  :root {
    --page: #ffffff;
    --card: #2a2a2a;
    --card-edge: #d6d6d6;
    --ink: #ffffff;
    --band-start: #5b6c7a;
    --band-end: #2a2a2a;
    --glow: rgba(205, 205, 205, 0.38);
    --glow-fade: rgba(42, 42, 42, 0);
  }
  html, body {
    margin: 0;
    padding: 0;
    overflow: hidden;
  }
  body {
    width: 945px;
    height: 1200px;
    background: var(--page);
    position: relative;
  }
  .card {
    position: absolute;
    left: 48px;
    width: 855px;
    height: 540px;
    background: var(--card);
    border-radius: 44px;
    box-shadow: 0 0 0 2px var(--card-edge), 0 3px 8px rgba(0,0,0,0.25);
    overflow: hidden;
  }
  .card--front { top: 38px; }
  .card--back { top: 627px; }

  .brand-name {
    position: absolute;
    left: 0;
    right: 0;
    top: 200px;
    margin: 0;
    text-align: center;
    font-family: "Montserrat", sans-serif;
    font-weight: 300;
    font-size: 96px;
    letter-spacing: 2px;
    line-height: 1;
    color: var(--ink);
  }
  .web-band {
    position: absolute;
    left: 18px;
    top: 410px;
    width: 430px;
    height: 48px;
    background: linear-gradient(90deg, var(--band-start), var(--band-end));
  }
  .web-address {
    position: absolute;
    left: 203px;
    top: 412px;
    margin: 0;
    font-family: "Montserrat", sans-serif;
    font-weight: 300;
    font-size: 29px;
    letter-spacing: 1.5px;
    line-height: 44px;
    color: var(--ink);
  }

  .contact-list {
    position: absolute;
    left: 87px;
    top: 122px;
    margin: 0;
    padding: 0;
    list-style: none;
    font-family: "Oswald", sans-serif;
    font-weight: 300;
    font-size: 40px;
    line-height: 58px;
    color: var(--ink);
  }
  .film-art {
    position: absolute;
    left: 399px;
    top: 40px;
    width: 410px;
    height: 450px;
    background: radial-gradient(ellipse 55% 60% at 48% 40%, var(--glow), var(--glow-fade) 100%);
  }
</style>
</head>
<body>
  <section class="card card--front">
    <h1 class="brand-name">lumora studio</h1>
    <div class="web-band"></div>
    <p class="web-address">www.lumorastudio.com.au</p>
  </section>

  <section class="card card--back">
    <ul class="contact-list">
      <li>Comapany name</li>
      <li>Address</li>
      <li>Sample name</li>
      <li>Phone#</li>
      <li>Website</li>
    </ul>
    <div class="film-art" role="img" aria-label="Soft grey film strip graphic fading into the dark card"></div>
  </section>
</body>
</html>
```